Harwell Lawyers Banner

I would like to have a graphic design created for a company banner. The company is Harwell Lawyers and the website is https://harwelllawyers-example.com.au/ We would like a professional banner we are able to put up at events to advertise the company.
The banner size is 800mm wide by 2000mm high so please keep the design inside these constraints.

```html
<!DOCTYPE html>
<html lang="en">
<head>
<meta charset="utf-8">
<title>Harwell Lawyers – Event Banner</title>
<link rel="stylesheet" href="https://fonts.googleapis.com/css2?family=Montserrat:wght@400;500;600;700;800&display=swap">
<style>
  :root {
    --backdrop: #8e8e8e;
    --paper: #ffffff;
    --paper-shade: #ededed;
    --ink: #2b2b2b;
    --ink-soft: #4d4d4d;
    --brand-blue: #29a0d6;
    --brand-yellow: #f7b418;
    --panel-dark: #2a2a2a;
    --panel-dark-2: #333333;
    --text-light: #ffffff;
  }
  * { box-sizing: border-box; margin: 0; padding: 0; }
  html, body {
    width: 1200px; height: 2312px; overflow: hidden;
    background: var(--backdrop);
    font-family: "Montserrat", Arial, sans-serif;
  }
  .banner {
    position: absolute; left: 170px; top: 81px;
    width: 860px; height: 2150px;
    background: var(--paper);
    display: flex; flex-direction: column;
    box-shadow: 0 6px 24px rgba(0,0,0,.18);
  }
  .brand-header {
    height: 372px; display: flex; align-items: center; justify-content: center; gap: 22px;
  }
  .brand-mark {
    width: 26px; height: 26px; background: var(--brand-blue);
  }
  .brand-name {
    font-weight: 400; font-size: 62px; letter-spacing: 4px; color: var(--ink);
    white-space: nowrap;
  }
  .intro-band {
    position: relative; height: 197px; background: var(--brand-blue);
    display: flex; align-items: center; padding: 0 40px 0 68px;
  }
  .intro-band::before {
    content: ""; position: absolute; left: 68px; top: 38px; bottom: 38px;
    width: 6px; background: var(--text-light);
  }
  .intro-band::after {
    content: ""; position: absolute; left: 128px; bottom: -22px;
    border-left: 22px solid transparent; border-right: 22px solid transparent;
    border-top: 22px solid var(--brand-blue); z-index: 2;
  }
  .intro-text {
    margin-left: 46px; color: var(--text-light); font-weight: 700;
    font-size: 35px; line-height: 1.35;
  }
  .team-photo {
    height: 560px;
    background: linear-gradient(100deg, #cfd3d4 0%, #a9b1b6 30%, #4a5868 55%, #2e3a4d 75%, #3b4658 100%);
  }
  .specialties {
    height: 333px; background: linear-gradient(90deg, var(--panel-dark), var(--panel-dark-2));
    padding: 32px 0 0 74px;
  }
  .specialties h2 {
    color: var(--brand-yellow); font-weight: 700; font-size: 28px; letter-spacing: 5px;
    margin-bottom: 10px;
  }
  .specialties ul { list-style: none; }
  .specialties li {
    display: flex; align-items: center; gap: 20px;
    color: var(--text-light); font-weight: 600; font-size: 23px; line-height: 34.5px;
  }
  .specialties svg { width: 17px; height: 17px; flex: none; }
  .services {
    flex: 1; position: relative;
    background: linear-gradient(180deg, var(--paper) 0%, var(--paper-shade) 100%);
    padding: 42px 0 0 80px;
  }
  .services h2 {
    font-weight: 800; font-size: 48px; color: var(--ink); margin-bottom: 26px;
  }
  .services ul { list-style: none; }
  .services li {
    position: relative; padding-left: 38px; font-weight: 500; font-size: 23px;
    color: var(--ink-soft); line-height: 35px; margin-bottom: 5px; max-width: 460px;
  }
  .services li::before {
    content: "»"; position: absolute; left: 0; top: -2px;
    color: var(--brand-blue); font-weight: 800; font-size: 30px;
  }
  .contact {
    position: absolute; left: 0; right: 0; top: 535px; text-align: center;
  }
  .contact-phone {
    display: inline-flex; align-items: center; gap: 10px;
    font-weight: 800; font-size: 58px; color: var(--ink);
  }
  .contact-phone svg { width: 32px; height: 32px; }
  .contact-web {
    display: flex; align-items: center; justify-content: center; gap: 12px;
    margin-top: 6px; font-size: 20px; letter-spacing: 3px; color: var(--ink);
  }
  .contact-web svg { width: 30px; height: 30px; }
  .contact-web b { font-weight: 700; }
  .footer-bar {
    position: absolute; bottom: 0; left: 300px; width: 260px; height: 14px;
    background: var(--brand-yellow);
  }
</style>
</head>
<body>
<main class="banner">
  <header class="brand-header">
    <span class="brand-mark"></span>
    <span class="brand-name">HARWELL LAWYERS</span>
  </header>

  <section class="intro-band">
    <p class="intro-text">Harwell Lawyers is a leading commercial law firm located in Logan City, Queensland.</p>
  </section>

  <div class="team-photo" role="img" aria-label="Photo of two lawyers in suits reviewing a tablet in an office, with colleagues at a meeting table behind them"></div>

  <section class="specialties">
    <h2>SPECIALISING IN:</h2>
    <ul>
      <li><svg viewBox="0 0 16 16"><rect x="1" y="3" width="11" height="11" fill="none" stroke="#f7b418" stroke-width="1.6"/><path d="M4 8l3 3 8-9" fill="none" stroke="#f7b418" stroke-width="2"/></svg>Advising Family Businesses</li>
      <li><svg viewBox="0 0 16 16"><rect x="1" y="3" width="11" height="11" fill="none" stroke="#f7b418" stroke-width="1.6"/><path d="M4 8l3 3 8-9" fill="none" stroke="#f7b418" stroke-width="2"/></svg>Estate Planning, Administration and Disputes</li>
      <li><svg viewBox="0 0 16 16"><rect x="1" y="3" width="11" height="11" fill="none" stroke="#f7b418" stroke-width="1.6"/><path d="M4 8l3 3 8-9" fill="none" stroke="#f7b418" stroke-width="2"/></svg>Tax and Structuring</li>
      <li><svg viewBox="0 0 16 16"><rect x="1" y="3" width="11" height="11" fill="none" stroke="#f7b418" stroke-width="1.6"/><path d="M4 8l3 3 8-9" fill="none" stroke="#f7b418" stroke-width="2"/></svg>Planning and Environment</li>
      <li><svg viewBox="0 0 16 16"><rect x="1" y="3" width="11" height="11" fill="none" stroke="#f7b418" stroke-width="1.6"/><path d="M4 8l3 3 8-9" fill="none" stroke="#f7b418" stroke-width="2"/></svg>Not for Profit and Social Enterprise</li>
      <li><svg viewBox="0 0 16 16"><rect x="1" y="3" width="11" height="11" fill="none" stroke="#f7b418" stroke-width="1.6"/><path d="M4 8l3 3 8-9" fill="none" stroke="#f7b418" stroke-width="2"/></svg>Management Rights, Property &amp; Developments</li>
      <li><svg viewBox="0 0 16 16"><rect x="1" y="3" width="11" height="11" fill="none" stroke="#f7b418" stroke-width="1.6"/><path d="M4 8l3 3 8-9" fill="none" stroke="#f7b418" stroke-width="2"/></svg>Litigation &amp; Dispute Resolution</li>
    </ul>
  </section>

  <section class="services">
    <h2>WHAT WE DO</h2>
    <ul>
      <li>Advising Family Businesses</li>
      <li>Tax and Structuring</li>
      <li>Planning and Environment</li>
      <li>Not For Profit and Social Enterprise</li>
      <li>Litigation and Dispute Resolution</li>
      <li>Estate Planning, Administration and Disputes</li>
      <li>Management Rights, Property and Developments</li>
    </ul>

    <div class="contact">
      <div class="contact-phone">
        <svg viewBox="0 0 24 24"><path d="M6.6 10.8a15 15 0 0 0 6.6 6.6l2.2-2.2a1 1 0 0 1 1-.25 11.4 11.4 0 0 0 3.6.57 1 1 0 0 1 1 1V20a1 1 0 0 1-1 1A17 17 0 0 1 3 4a1 1 0 0 1 1-1h3.5a1 1 0 0 1 1 1c0 1.25.2 2.45.57 3.57a1 1 0 0 1-.25 1z" fill="#2b2b2b"/></svg>
        07 3184 5520
      </div>
      <div class="contact-web">
        <svg viewBox="0 0 24 24"><circle cx="12" cy="12" r="10.5" fill="none" stroke="#2b2b2b" stroke-width="1.4"/><circle cx="12" cy="12" r="7" fill="none" stroke="#2b2b2b" stroke-width="1.2"/><ellipse cx="12" cy="12" rx="3" ry="7" fill="none" stroke="#2b2b2b" stroke-width="1"/><path d="M5 12h14M6 8.5h12M6 15.5h12" stroke="#2b2b2b" stroke-width="1"/></svg>
        <span>WWW.<b>HARWELLLAWYERS-EXAMPLE</b>.COM.AU</span>
      </div>
    </div>

    <div class="footer-bar"></div>
  </section>
</main>
</body>
</html>
```